I need a design with just the number 24. must be in blue color (royal blue) should be large enough for people see must be in the center of page. Place a nice border around the page.

• Number 24 in Royal blue color

```html
<!DOCTYPE html>
<html lang="en">
<head>
<meta charset="UTF-8">
<title>24</title>
<link rel="stylesheet" href="https://fonts.googleapis.com/css2?family=Oswald:wght@700&display=swap">
<style>
  :root {
    --royal-blue: #0000ff;
    --paper: #ffffff;
  }
  html, body {
    margin: 0;
    padding: 0;
    width: 960px;
    height: 1200px;
    overflow: hidden;
    background: var(--paper);
  }
  .sign {
    position: relative;
    width: 960px;
    height: 1200px;
    box-sizing: border-box;
    background: var(--paper);
    border: 29px solid var(--royal-blue);
  }
  .sign__rule {
    position: absolute;
    inset: 13px;
    border: 2px solid var(--royal-blue);
  }
  .sign__number {
    position: absolute;
    inset: 0;
    display: flex;
    align-items: center;
    justify-content: center;
    margin: 0;
    padding-top: 16px;
    font-family: "Oswald", "Arial Narrow", sans-serif;
    font-weight: 700;
    font-size: 770px;
    line-height: 1;
    letter-spacing: -12px;
    color: var(--royal-blue);
  }
</style>
</head>
<body>
  <main class="sign">
    <div class="sign__rule"></div>
    <h1 class="sign__number">24</h1>
  </main>
</body>
</html>
```